Christmas Party Poster

I am promoting a Christmas Party for teenagers age 13-17 years old. The event is the first of its kind in our area, Weston Super Mare. The ticket price is to include food, soft drink's, music, entertainment.

There is nothing else of its kind in the the area or surrounding towns so a one of a kind event and new to the town. I would like the poster to be as simple and less busy as possible while still clearly showing the key information, anything that can be added it to show its a Christmas party for teenagers would be great. Also this is aimed at 13-17 year old's so as current and modern a design as possible.
Updates

A big thank you for the designs so far, As this is my first project I'm just getting the hang of what to ask for. I have slightly updated the brief and I now realize less is more, so long as the poster has the key elements of event name, date, time's, location, price and age range. The rest I should have been more flexible on. Thank you for your patience.

Target Market(s)

My Target Market are teenagers specifically 13-17 year olds

Industry/Entity Type

Town

Requirements
Must have
• The Title 'Frostgleam' The venue is 'The Amber Pavilion h-b-t', Phone Number '01852 630284' Date '19th December'. Times '19.00 - 23.00'. Strictly u18 or age 13-17 years. Ticket price of £20. Friendwall 'frost gleam hbt' limited 4 tickets per person
Nice to have
• Christmas Party, Photo of your night out. Food and drink included
Should not have
• no worded reference to Santa, snowmen, reindeer, disco, try to keep out as not to offend cool teenagers.

```html
<!DOCTYPE html>
<html lang="en">
<head>
<meta charset="utf-8">
<title>Frostgleam – Christmas Party Poster</title>
<link rel="stylesheet" href="https://fonts.googleapis.com/css2?family=Bowlby+One&family=Bangers&family=Nunito:wght@800;900&display=swap">
<style>
  :root {
    --page: #f1f1f1;
    --paper: #ffffff;
    --ice-deep: #0a6fb8;
    --ice-mid: #2aa3e0;
    --ice-light: #8fd6f6;
    --frost: #e9f8ff;
    --navy: #0b2f73;
    --ribbon: #1f4fa8;
    --ribbon-dark: #0f2f6e;
    --gold: #f7a21a;
    --gold-dark: #c9650a;
    --white: #ffffff;
  }
  * { margin: 0; padding: 0; box-sizing: border-box; }
  html, body { width: 1200px; height: 848px; overflow: hidden; }
  body { background: var(--page); position: relative; }

  .poster {
    position: absolute; left: 339px; top: 20px;
    width: 521px; height: 808px;
    background: var(--paper);
    box-shadow: 0 4px 14px rgba(0,0,0,.18);
  }
  .poster__art {
    position: absolute; left: 6px; top: 6px; right: 6px; bottom: 18px;
    background:
      radial-gradient(ellipse at 15% 10%, rgba(255,255,255,.7) 0%, transparent 30%),
      radial-gradient(ellipse at 90% 45%, rgba(255,255,255,.55) 0%, transparent 30%),
      linear-gradient(180deg, #5cc3f0 0%, var(--ice-mid) 50%, #5cc3f0 100%);
    overflow: hidden;
  }
  .panel {
    position: absolute; left: 28px; top: 60px; width: 453px; height: 691px;
    border-radius: 18px;
    background: linear-gradient(180deg, #3fb2ec 0%, #2f9fdf 40%, #4cbcef 62%, #2e9ddc 100%);
    box-shadow: inset 0 0 0 1px rgba(255,255,255,.35);
  }
  .ribbon { position: absolute; }
  .ribbon--top { left: 14px; top: 46px; }
  .ribbon--bottom { right: 14px; bottom: 10px; }

  .festive-scene {
    position: absolute; left: 30px; top: 150px; width: 460px; height: 320px;
    border-radius: 46% 54% 40% 60% / 50% 45% 55% 50%;
    background:
      radial-gradient(circle at 18% 78%, #1668c4 0%, #2f8fe0 14%, transparent 22%),
      radial-gradient(circle at 86% 70%, #0d3f8f 0%, #1e5fbf 10%, transparent 17%),
      radial-gradient(circle at 78% 18%, #1a72d0 0%, transparent 12%),
      radial-gradient(ellipse at 50% 48%, #ffffff 0%, #e3f5ff 30%, #a9def8 55%, rgba(60,160,230,.6) 75%, transparent 90%),
      linear-gradient(160deg, transparent 55%, rgba(255,255,255,.85) 64%, transparent 72%);
  }

  .price-badge { position: absolute; left: 64px; top: 58px; width: 128px; height: 120px; }
  .price-badge__label {
    position: absolute; inset: 0; display: flex; align-items: center; justify-content: center;
    font-family: "Nunito", sans-serif; font-weight: 900; font-size: 40px; color: var(--white);
    transform: rotate(-14deg); text-shadow: 0 2px 3px rgba(120,50,0,.6);
  }

  .event-when {
    position: absolute; left: 270px; top: 66px; width: 200px; text-align: center;
    font-family: "Nunito", sans-serif; font-weight: 900; color: var(--white);
    text-shadow: 0 0 6px rgba(0,60,140,.7);
  }
  .event-when__date { font-size: 16px; line-height: 20px; }
  .event-when__time { font-size: 20px; line-height: 22px; }

  .event-title {
    position: absolute; left: 0; right: 0; top: 196px; text-align: center;
    font-family: "Bowlby One", sans-serif; font-size: 76px; line-height: 74px;
    color: var(--frost);
    -webkit-text-stroke: 4px var(--ice-deep);
    paint-order: stroke fill;
    text-shadow: 0 0 16px rgba(255,255,255,.95), 0 5px 0 var(--navy);
    letter-spacing: 1px;
  }

  .highlights {
    position: absolute; left: 0; right: 0; top: 488px; text-align: center;
    font-family: "Nunito", sans-serif; font-weight: 900; color: var(--white);
    text-shadow: 0 0 5px rgba(0,70,150,.6);
  }
  .highlights__main { font-size: 23px; line-height: 25px; }
  .highlights__sub { font-size: 18px; line-height: 22px; }

  .age-limit {
    position: absolute; left: 0; right: 0; top: 590px; text-align: center;
    font-family: "Nunito", sans-serif; font-weight: 900; font-size: 15px; line-height: 19px;
    color: var(--white);
  }
  .venue {
    position: absolute; left: 0; right: 0; top: 626px; text-align: center;
    font-family: "Bangers", sans-serif; font-size: 44px; letter-spacing: 1px;
    color: var(--white); text-shadow: 0 0 10px rgba(255,255,255,.9), 0 0 4px var(--ice-deep);
  }
  .box-office {
    position: absolute; left: 0; right: 0; top: 694px; text-align: center;
    font-family: "Nunito", sans-serif; font-weight: 900; font-size: 18px;
    color: var(--white); text-shadow: 0 0 6px var(--navy);
  }
  .small-print {
    position: absolute; left: 0; right: 0; top: 728px; text-align: center;
    font-family: "Nunito", sans-serif; font-weight: 900; font-size: 10px; line-height: 13px;
    color: var(--white);
  }
  .social-handle { display: inline-flex; align-items: center; gap: 4px; margin-left: 6px; }
  .social-handle__mark { width: 10px; height: 10px; background: var(--white); display: inline-block; }
</style>
</head>
<body>
  <main class="poster">
    <div class="poster__art">
      <div class="panel"></div>

      <svg class="ribbon ribbon--top" width="90" height="80" viewBox="0 0 90 80" aria-hidden="true">
        <polygon points="0,40 40,0 60,0 0,60" fill="var(--ribbon)"/>
        <polygon points="0,60 60,0 66,0 0,66" fill="var(--ribbon-dark)"/>
      </svg>
      <svg class="ribbon ribbon--bottom" width="120" height="160" viewBox="0 0 120 160" aria-hidden="true">
        <polygon points="120,0 120,28 28,160 0,160" fill="var(--ribbon)"/>
        <polygon points="120,28 120,36 34,160 28,160" fill="var(--ribbon-dark)"/>
      </svg>

      <div class="festive-scene" role="img" aria-label="Illustration of blue Christmas baubles, stars, bead strings, a white light flare and party speakers around the title"></div>

      <div class="price-badge">
        <svg width="128" height="120" viewBox="0 0 128 120" aria-hidden="true">
          <defs>
            <linearGradient id="badgeFill" x1="0" y1="0" x2="0" y2="1">
              <stop offset="0" stop-color="var(--gold)"/>
              <stop offset="1" stop-color="var(--gold-dark)"/>
            </linearGradient>
          </defs>
          <polygon fill="url(#badgeFill)" stroke="#fff3c8" stroke-width="1.5"
            points="64,4 74,18 92,10 95,28 114,28 108,46 124,58 108,70 114,88 95,88 92,106 74,98 64,114 54,98 36,106 33,88 14,88 20,70 4,58 20,46 14,28 33,28 36,10 54,18"/>
        </svg>
        <span class="price-badge__label">£20</span>
      </div>

      <div class="event-when">
        <p class="event-when__date">19TH DECEMBER</p>
        <p class="event-when__time">19.00PM<br>TO 23.00PM</p>
      </div>

      <h1 class="event-title">FROST<br>GLEAM</h1>

      <div class="highlights">
        <p class="highlights__main">THE BEST MUSIC,TOP TUNES</p>
        <p class="highlights__main">ENTERTAINMENT</p>
        <p class="highlights__sub">PHOTO OF YOUR NIGHT OUT</p>
      </div>

      <p class="age-limit">STRICTLY<br>U18 OR AGE 13-17 YEARS OLD</p>

      <p class="venue">THE AMBER PAVILION</p>

      <p class="box-office">CONTACT BOX OFFICE( 01852) 630284</p>

      <div class="small-print">
        <p>FIND US ON FRIENDWALL
          <span class="social-handle"><span class="social-handle__mark"></span>FROST GLEAM HBT</span>
        </p>
        <p>LIMITED 4 TICKETS PER PERSON</p>
      </div>
    </div>
  </main>
</body>
</html>
```